Flyer Design Project

We need a flyer (in Spanish) for:
"Feria Cántaro & Telar Brisa Alta 2013"
This event will be held in Los Angeles CA and would like to attract exhibitors.
Must include the information provided in the word file.
Updates

Target Market(s)

Tequila producers and distributors

Industry/Entity Type

Event

Requirements
Must have
• pictures to be used at your discretion

```html
<!DOCTYPE html>
<html lang="es">
<head>
<meta charset="utf-8">
<title>Feria Cántaro &amp; Telar Brisa Alta 2013 — Folleto</title>
<link href="https://fonts.googleapis.com/css2?family=Arimo:wght@400;700&family=Lilita+One&display=swap" rel="stylesheet">
<style>
  :root{
    --bg:#3a3a3a;
    --page:#2d2d2d;
    --page-deep:#232323;
    --lime:#8cc63f;
    --yellow:#f5e400;
    --olive:#5d6b12;
    --cyan:#00aeef;
    --magenta:#ec008c;
    --red:#e8261c;
    --green:#17a94b;
    --white:#ffffff;
    --ink:#1a1a1a;
  }
  *{box-sizing:border-box;margin:0;padding:0}
  html,body{width:1200px;height:947px;overflow:hidden;background:var(--bg)}
  body{position:relative;font-family:"Arimo",Arial,sans-serif;color:var(--white)}

  .sheet{position:absolute;background:var(--page);box-shadow:0 6px 18px rgba(0,0,0,.45);overflow:hidden}

  /* Portada */
  .cover{left:30px;top:30px;width:290px;height:432px}
  .cover-art{position:absolute;left:0;top:34px;width:100%;height:332px;
    background:
      radial-gradient(ellipse 60% 45% at 85% 15%, rgba(0,174,239,.9), transparent 70%),
      radial-gradient(ellipse 55% 40% at 90% 60%, rgba(236,0,140,.85), transparent 70%),
      radial-gradient(ellipse 50% 35% at 10% 40%, rgba(245,228,0,.9), transparent 70%),
      radial-gradient(ellipse 40% 50% at 50% 35%, rgba(60,60,60,.7), transparent 70%),
      linear-gradient(160deg,#d8e800 0%,#8cc63f 45%,#f08ac8 80%,#b8e04a 100%)}
  .cover-title{position:absolute;left:14px;top:232px;width:262px;font-family:"Lilita One",Impact,sans-serif;line-height:1}
  .cover-title .kicker{font-size:20px;color:var(--olive)}
  .cover-title .main{font-size:27px;color:var(--yellow);text-shadow:2px 2px 0 var(--olive)}
  .cover-title .place{font-size:21px;color:var(--olive);text-align:right;margin-top:2px}
  .cover-dates{position:absolute;left:0;width:100%;top:326px;text-align:center;font-family:"Lilita One",Impact,sans-serif;font-size:14px;color:var(--ink)}
  .cover-year{position:absolute;left:84px;top:347px;width:122px;height:42px;background:var(--page-deep);
    font-family:"Lilita One",Impact,sans-serif;font-size:32px;color:var(--yellow);text-align:center;line-height:42px}

  /* Contraportada */
  .back{left:30px;top:487px;width:290px;height:430px;background:#333333}
  .back-art{position:absolute;left:78px;top:240px;width:134px;height:80px;
    background:radial-gradient(ellipse 60% 70% at 50% 100%, #b6e04a, #4f8f1c 60%, transparent 80%)}
  .back-info{position:absolute;left:0;top:328px;width:100%;text-align:center;font-size:9px;line-height:1.35}
  .back-info .lead{font-weight:700;margin-bottom:5px}
  .back-info .region{margin-top:5px}
  .back-info .tel{text-align:left;padding-left:66px;margin-top:2px;color:#cfcfcf}

  /* Interior */
  .spread{left:360px;top:170px;width:810px;height:608px;background:transparent;box-shadow:none;overflow:visible}
  .page{position:absolute;top:0;width:405px;height:608px;background:var(--page);box-shadow:0 6px 18px rgba(0,0,0,.45);overflow:hidden}
  .page-left{left:0}
  .page-right{left:405px;border-left:1px solid #444}

  .stripes{position:absolute;left:0;width:100%;
    background:linear-gradient(100deg,var(--lime) 0 18%,var(--magenta) 18% 34%,var(--yellow) 34% 50%,#5fb63a 50% 64%,var(--cyan) 64% 80%,var(--yellow) 80% 100%)}
  .stripes-top{top:0;height:122px}
  .stripes-bottom{top:420px;height:90px;clip-path:polygon(0 0,100% 0,80% 100%,0 100%)}
  .photo-frame{position:absolute;left:28px;top:118px;width:354px;height:310px;background:var(--white);padding:14px 16px 22px}
  .photo{width:100%;height:100%;background:linear-gradient(135deg,#6b4a3a,#b98c6a 45%,#3d4f6a 80%,#222)}
  .note{position:absolute;left:62px;top:500px;width:330px;height:96px;background:var(--white);color:var(--ink);
    transform:rotate(-6deg);padding:12px 16px;font-size:11px;line-height:1.3}

  .panel{position:absolute;left:30px;width:345px;padding:10px 16px;font-size:10.5px;line-height:1.32;color:var(--white);text-align:center}
  .panel-1{top:19px;background:var(--lime);transform:rotate(-1.2deg)}
  .panel-2{top:125px;background:var(--cyan);transform:rotate(.8deg)}
  .panel-3{top:247px;background:var(--magenta);transform:rotate(-.8deg);padding:14px 16px}
  .panel-4{top:382px;background:var(--red);transform:rotate(1deg)}
  .panel-5{top:479px;background:var(--green);transform:rotate(-1deg);padding:12px 16px}
</style>
</head>
<body>

<section class="sheet cover" aria-label="Portada">
  <div class="cover-art" role="img" aria-label="Ilustración de mujer con penacho de plumas sobre remolinos de colores verde, cian, amarillo y magenta"></div>
  <h1 class="cover-title">
    <span class="kicker">FERIA</span><br>
    <span class="main">Cántaro &amp; Telar</span>
    <div class="place">Brisa Alta</div>
  </h1>
  <p class="cover-dates">29 y 30 de agosto</p>
  <p class="cover-year">2013</p>
</section>

<section class="sheet back" aria-label="Contraportada">
  <div class="back-art" role="img" aria-label="Ilustración de planta de agave verde"></div>
  <div class="back-info">
    <p class="lead">Para oportunidades de patrocinio y exhibición:</p>
    <p class="region">En Estados Unidos:</p>
    <p>Ramiro E. Quintana – Director</p>
    <p>rquintana@feriabrisa.com</p>
    <p class="region">En Mexico:</p>
    <p>Ing. Julián P. Ordaz</p>
    <p class="tel">Tel. 555-0142 &nbsp;&nbsp; jordaz@feriabrisa.com</p>
  </div>
</section>

<section class="sheet spread" aria-label="Interior">
  <div class="page page-left">
    <div class="stripes stripes-top" role="img" aria-label="Franjas diagonales de colores con planta de agave y círculos concéntricos"></div>
    <div class="stripes stripes-bottom" role="img" aria-label="Franjas de colores con círculos concéntricos"></div>
    <div class="photo-frame">
      <div class="photo" role="img" aria-label="Fotografía de un grupo de amigos brindando con caballitos de tequila"></div>
    </div>
    <p class="note">Cuando buscamos qué beber, buscamos en el mundo, y ese mundo termina en nuestros vasos. Queremos lo mejor, lo más sabroso, lo interesante y estamos dispuestos a recorrer grandes distancias para obtenerlo.</p>
  </div>
  <div class="page page-right">
    <p class="panel panel-1">La promoción y la creatividad son, quizás lo más importante en tiempos de incertidumbre económica, cuando se es implacable en la búsqueda de nuevos clientes.</p>
    <p class="panel panel-2">Con una perspectiva más amplia más globales, ya sea tradiciones centenarias, o la exploración de las fronteras de las bebidas de moda, buscando nuevos mercados, o re-inventando su marca para mantenerse competitivos.</p>
    <p class="panel panel-3">En esta edición especializada en Tequila vamos a discutir las técnicas, procesos creativos, perfiles de sabor, tecnologías, y los ingredientes que son cada vez más esenciales de la caja de herramientas del Coctelero (Mixologist) del siglo 21.</p>
    <p class="panel panel-4">Tendremos una competencia de las cuatro variedades de tequila: Blanco, Reposado, Añejo y Extra Añejo; con reconocimiento a los ganadores de cada categoría.</p>
    <p class="panel panel-5">Acompáñanos, los días 29 y 30 de agosto 2013, donde se vincularan consumidores, bares, detallistas, restaurantes y distribuidores en la matriz de creatividad coctelera tablero culinario, sabores de moda y uno de los mercados más importantes e influyentes del mundo.</p>
  </div>
</section>

</body>
</html>
```